Back Pain

Need a flyer similar to the attached draft. This is to be handed out to prospective patients. Note that Artwell Studio has already designed the logo. If you need a copy please contact me

```html
<!DOCTYPE html>
<html lang="en">
<head>
<meta charset="utf-8">
<title>Spine Ease Clinic Flyer</title>
<link href="https://fonts.googleapis.com/css2?family=Montserrat:wght@400;500;600;700;800&display=swap" rel="stylesheet">
<style>
  :root {
    --page-bg: #e8e5e1;
    --ink-black: #000000;
    --brand-blue: #0a9ad6;
    --brand-lime: #b7dc55;
    --soft-grey: #c9c9c9;
    --white: #ffffff;
  }
  * { margin: 0; padding: 0; box-sizing: border-box; }
  html, body {
    width: 1184px; height: 1200px; overflow: hidden;
    background: var(--page-bg);
    font-family: "Montserrat", sans-serif;
  }
  .flyer {
    position: absolute; left: 184px; top: 25px;
    width: 815px; height: 1150px; overflow: hidden;
    background: var(--ink-black);
  }
  .flyer-art { position: absolute; inset: 0; }
  .clinic-name {
    position: absolute; left: 0; width: 100%; top: 616px;
    text-align: center; color: var(--brand-blue);
    font-weight: 600; font-size: 31px; letter-spacing: -0.5px;
  }
  .clinic-tagline {
    position: absolute; left: 0; width: 100%; top: 656px;
    text-align: center; color: var(--brand-lime);
    font-weight: 600; font-size: 14px; letter-spacing: 4.2px;
  }
  .conditions {
    position: absolute; top: 735px; list-style: none;
    color: var(--soft-grey); font-size: 34px; font-weight: 400; line-height: 40px;
  }
  .conditions li { position: relative; padding-left: 28px; }
  .conditions li::before {
    content: ""; position: absolute; left: 0; top: 14px;
    width: 9px; height: 9px; border-radius: 50%; background: var(--brand-blue);
  }
  .conditions--left { left: 67px; }
  .conditions--right { left: 425px; }
  .practitioner {
    position: absolute; left: 42px; top: 952px; color: var(--white);
  }
  .practitioner-name { font-size: 35px; font-weight: 800; line-height: 38px; letter-spacing: -0.5px; }
  .practitioner-note { font-size: 26px; font-weight: 400; line-height: 34px; }
  .contact-divider {
    position: absolute; left: 347px; top: 969px; width: 2px; height: 60px; background: var(--white);
  }
  .contact-details {
    position: absolute; left: 372px; top: 965px; color: var(--white);
    font-size: 22px; line-height: 33px; font-weight: 400;
  }
  .offer-box {
    position: absolute; left: 22px; top: 1054px; width: 770px; height: 85px;
    background: var(--brand-lime); border-radius: 6px;
    display: flex; flex-direction: column; justify-content: center; align-items: center;
    color: var(--ink-black); font-weight: 700; font-size: 26px; line-height: 34px;
  }
</style>
</head>
<body>
<main class="flyer">
  <svg class="flyer-art" width="815" height="1150" viewBox="0 0 815 1150">
    <defs>
      <linearGradient id="heroRoom" x1="0" y1="0" x2="1" y2="0">
        <stop offset="0" stop-color="#e9ecec"/>
        <stop offset="0.14" stop-color="#dfe2dc"/>
        <stop offset="0.2" stop-color="#b8876a"/>
        <stop offset="0.5" stop-color="#9c6a4f"/>
        <stop offset="0.78" stop-color="#b07c60"/>
        <stop offset="0.86" stop-color="#e4e6e6"/>
        <stop offset="1" stop-color="#f3f4f4"/>
      </linearGradient>
      <linearGradient id="heroShade" x1="0" y1="0" x2="0" y2="1">
        <stop offset="0" stop-color="#ffffff" stop-opacity="0.18"/>
        <stop offset="0.6" stop-color="#ffffff" stop-opacity="0"/>
        <stop offset="1" stop-color="#3a2418" stop-opacity="0.35"/>
      </linearGradient>
      <linearGradient id="jointTone" x1="0" y1="0" x2="1" y2="1">
        <stop offset="0" stop-color="#ecebef"/>
        <stop offset="0.55" stop-color="#d9b19c"/>
        <stop offset="1" stop-color="#c98f75"/>
      </linearGradient>
      <linearGradient id="jointToneAlt" x1="1" y1="0" x2="0" y2="1">
        <stop offset="0" stop-color="#ecebef"/>
        <stop offset="0.55" stop-color="#d9b19c"/>
        <stop offset="1" stop-color="#c98f75"/>
      </linearGradient>
    </defs>
    <g class="hero-photo" role="img" aria-label="Photo of a chiropractor adjusting a patient's upper back, with a red pain highlight on the spine">
      <rect x="0" y="0" width="815" height="560" fill="url(#heroRoom)"/>
      <rect x="0" y="0" width="815" height="560" fill="url(#heroShade)"/>
    </g>
    <path d="M0 377 Q407 610 815 391 L815 1150 L0 1150 Z" fill="var(--ink-black)"/>
    <path d="M0 377 Q407 610 815 391" fill="none" stroke="var(--brand-lime)" stroke-width="5"/>
    <path d="M0 868 Q407 953 815 890 L815 1150 L0 1150 Z" fill="var(--brand-lime)"/>
    <path d="M0 888 Q407 957 815 898 L815 1150 L0 1150 Z" fill="var(--brand-blue)"/>

    <circle role="img" aria-label="Photo of an elbow with pain highlighted" cx="102" cy="418" r="68" fill="url(#jointTone)" stroke="var(--ink-black)" stroke-width="5"/>
    <circle role="img" aria-label="Photo of a neck and shoulder with pain highlighted" cx="263" cy="479" r="71" fill="url(#jointToneAlt)" stroke="var(--ink-black)" stroke-width="5"/>
    <circle cx="427" cy="528" r="82" fill="var(--ink-black)"/>
    <circle cx="427" cy="528" r="64" fill="none" stroke="var(--brand-blue)" stroke-width="6"/>
    <circle role="img" aria-label="Photo of a lower back with pain highlighted" cx="586" cy="473" r="68" fill="url(#jointTone)" stroke="var(--ink-black)" stroke-width="5"/>
    <circle role="img" aria-label="Photo of a wrist with pain highlighted" cx="733" cy="415" r="68" fill="url(#jointToneAlt)" stroke="var(--ink-black)" stroke-width="5"/>
  </svg>

  <h1 class="clinic-name">SPINE EASE CLINIC</h1>
  <p class="clinic-tagline">DR SAM WHITFORD - CHIROPRACTOR</p>

  <ul class="conditions conditions--left">
    <li>Headaches</li>
    <li>NeckPain</li>
    <li>ShoulderPain</li>
  </ul>
  <ul class="conditions conditions--right">
    <li>BackPain</li>
    <li>Arm&amp;HandPain</li>
    <li>Sciatica</li>
  </ul>

  <div class="practitioner">
    <p class="practitioner-name">DR. WHITFORD</p>
    <p class="practitioner-note">Now in Seaview AT</p>
  </div>
  <div class="contact-divider"></div>
  <div class="contact-details">
    <p>42 Harbour Street, Seaview 6200</p>
    <p>sam@spineeaseclinic.com.au</p>
  </div>

  <div class="offer-box">
    <p>50% Off Initial Consultation If you Book online at</p>
    <p>SPINEEASECLINIC.COM.AU | 0400 555 018</p>
  </div>
</main>
</body>
</html>
```